A resource brochure for seniors and their families/Brookline Care Partners

As we age, the journey can come with unexpected challenges and obstacles. Brookline Care Partners is here to provide seniors and their families with a road map to navigate those challenges and insure the journey is as smooth as possible. We are a company that offers 'one stop shop' resources for seniors who need assistance with selling their home, need home care support or need to find suitable senior housing living choices and much more. We need this brochure to showcase a caring, clear and clear way for families or individuals, many who have just lost a spouse/parent, to find resources during a very difficult and confusing time in their life. The final design should communicate caring support, a call to action (call us!), and showcase a professional and knowledgeable team that will gently support and be a guide to families and individuals who are trying to make big life choices within the senior care arena.

Target Market(s)

A mature market- SENIORS (75+) and their families (adult children 50+) who typically are going through life changes such as losing a spouse or having to make a move from their home into a Retirement Community.

Industry/Entity Type

Group

Font styles to use
Serif
Script

Requirements
Must have
• Showcase a thoughtful and caring mentality- 'we will take care of you" in a professional and knowledgeable way. Please make it clear what the message is - we can assist with selling a home, bringing support and care into the home, find more appropriate housing as well as any resources or tools needed throughout the senior care spectrum of resources. Must have our name, logo, website and address and we need one panel to be laid out as a mailer- our address on top left. (Please see attached rough draft for address- thank you!) Also- please keep the testimonial, which is attached inclusive of additional verbiage.
Nice to have
• An attractive senior (female) on the cover of the brochure with a 'What's Next?" feel to engage people to open the collateral and relate to the story and purpose of what we do. Showcase what our services are- we are a company that guides families to and through much needed resources as it relates to aging and the ever-changing needs of an elderly person. We want to be the experts and trusted by our clients and the tough decisions that come along with aging. We offer our referral services at no cost to our clients.
Should not have
• Should not sound slick, 'sales-y' or too pushy- we are trying to build a relationship and not 'over sell'...we want to be a trusted resource guide and a helping hand.

```html
<!DOCTYPE html>
<html lang="en">
<head>
<meta charset="utf-8">
<title>Brookline Care Partners – Inside Spread</title>
<link rel="stylesheet" href="https://fonts.googleapis.com/css2?family=Nunito:wght@700;800;900&family=Source+Sans+3:ital,wght@0,400;0,600;0,700;1,400&family=Kalam:wght@700&display=swap">
<style>
  :root{
    --page:#ffffff;
    --paper:#f7e4c9;
    --plum:#4b2e57;
    --ink:#2b2330;
    --orange:#f9a72a;
    --silver:#b9b9bb;
    --photo-a:#cfdbe6;
    --photo-b:#7f9fc4;
    --white:#ffffff;
  }
  *{box-sizing:border-box;margin:0;padding:0}
  html,body{width:1200px;height:1000px;overflow:hidden;background:var(--page)}
  body{font-family:"Source Sans 3",Arial,sans-serif;color:var(--ink);position:relative}
  .spread{position:absolute;left:74px;top:84px;width:1061px;height:819px;background:var(--paper)}
  .hero{position:absolute;left:74px;top:84px;width:406px;height:408px}
  .hero svg{display:block}
  .hero-tagline{position:absolute;left:28px;top:236px;width:170px;text-align:center;
    font-family:"Nunito",Arial,sans-serif;font-weight:800;font-size:19px;line-height:24.5px;color:var(--plum);
    text-shadow:-2px -2px 0 #fff,2px -2px 0 #fff,-2px 2px 0 #fff,2px 2px 0 #fff,0 2px 0 #fff,0 -2px 0 #fff,2px 0 0 #fff,-2px 0 0 #fff}
  .block{position:absolute;font-size:14.2px;line-height:19.2px;letter-spacing:-0.1px}
  .block p+p{margin-top:19px}
  .heading{font-family:"Nunito",Arial,sans-serif;font-weight:800;color:var(--plum);font-size:23px;line-height:28px}
  .intro{left:118px;top:508px;width:272px}
  .mission-title{position:absolute;left:118px;top:679px}
  .mission{left:118px;top:712px;width:262px}
  .goal{left:474px;top:146px;width:268px}
  .help-title{position:absolute;left:472px;top:393px}
  .help-box{position:absolute;left:469px;top:430px;width:269px;height:306px;background:var(--plum);border-radius:14px;padding:19px 14px 0 20px}
  .help-box ul{list-style:none;color:var(--white);font-weight:700;font-size:14.5px;line-height:20.2px}
  .help-box li{position:relative;padding-left:24px}
  .help-box li::before{content:"•";position:absolute;left:0}
  .quote{position:absolute;left:468px;top:744px;width:280px;font-family:"Kalam",cursive;font-weight:700;font-size:15.5px;line-height:23.5px;color:var(--ink)}
  .quote cite{display:block;text-align:right;padding-right:22px;font-style:normal}
  .testimonial-title{position:absolute;left:817px;top:139px;display:flex;align-items:center;width:267px}
  .testimonial-title .rule{flex:1;height:8px;background:var(--plum);margin-left:5px}
  .testimonial{left:818px;top:175px;width:264px;font-style:italic;font-size:12.6px;line-height:16px;letter-spacing:-0.15px}
  .testimonial p+p{margin-top:0}
  .testimonial .byline{text-align:right;padding-right:12px}
  .bar{position:absolute;left:818px;top:328px;width:263px;height:8px;background:var(--plum)}
  .right-title{position:absolute;left:817px}
  .right-text{left:818px;width:272px}
  .avail{list-style:none}
  .avail li{position:relative;padding-left:19px}
  .avail li::before{content:"•";position:absolute;left:0;font-size:12px}
</style>
</head>
<body>
  <div class="spread"></div>

  <div class="hero">
    <svg width="406" height="408" viewBox="0 0 406 408" xmlns="http://www.w3.org/2000/svg">
      <defs>
        <linearGradient id="photoTone" x1="0" y1="0" x2="1" y2="1">
          <stop offset="0" stop-color="var(--photo-a)"/>
          <stop offset="1" stop-color="var(--photo-b)"/>
        </linearGradient>
      </defs>
      <path role="img" aria-label="Photo of a smiling senior man shaking hands with an advisor" fill="url(#photoTone)" d="M0,0 H300 C322,150 250,330 0,382 Z"/>
      <path fill="var(--silver)" d="M360,0 H406 C396,190 310,345 110,398 C290,340 372,200 360,0 Z"/>
      <path fill="var(--orange)" d="M300,0 H366 C380,205 290,368 0,408 V382 C250,330 322,150 300,0 Z"/>
    </svg>
    <div class="hero-tagline">A helping<br>hand<br>during life’s<br>transitions . . .</div>
  </div>

  <div class="block intro">
    <p>During any major transition in life, we all could use a little help. We at Brookline Care Partners are here to assist you during these times when it is easy to become overwhelmed and confused with ‘what’s next?’ Whatever the newest challenge or question that may arise, call Brookline and let us work with you to find your best path forward.</p>
  </div>

  <h2 class="heading mission-title">Our Mission. . .</h2>
  <div class="block mission">
    <p>What started as an informal network has grown into something exceptional. This network of dedicated professionals share the same values, integrity, and mission to serve our seniors and their families with the highest level of integrity possible.</p>
  </div>

  <div class="block goal">
    <p>The goal, promise, and purpose of our network is to provide you with a simple and comprehensive path to help you navigate the challenges that arises as we all age. We look forward to serving you!</p>
    <p>As we age there are always new questions that arise. We at Brookline Care Partners have over 50 years of combined experience helping seniors and their families find their customized path to whatever comes next.</p>
  </div>

  <h2 class="heading help-title">Need help with . . .</h2>
  <div class="help-box">
    <ul>
      <li>Preparing a home for sale</li>
      <li>Downsizing</li>
      <li>Home maintenance and remodeling for accessibility</li>
      <li>Selling a home</li>
      <li>Bringing support into the home</li>
      <li>Finding senior living options</li>
      <li>Financial planning</li>
      <li>Estate pre-planning</li>
      <li>Funeral pre-planning</li>
      <li>Life insurance services</li>
      <li>Or anything else –</li>
    </ul>
  </div>

  <blockquote class="quote">
    “Never believe that a few caring people can’t change the world. For indeed, that’s all who ever have.”
    <cite>– Eleanor Hart –</cite>
  </blockquote>

  <h2 class="heading testimonial-title">Testimonial<span class="rule"></span></h2>
  <div class="block testimonial">
    <p>“After Dad passed away, the team at Brookline Care Partners came to the rescue. We really appreciate the resouces and time Daniel spent with us as we, as a family, were experiencing such a difficult time, a loss of my Dad and needing to find a new home for Mom. I highly recommend your services and by the way, Mom loves her new community and has made several friends.”</p>
    <p class="byline">– Marcus, Lakewood, USA</p>
  </div>
  <div class="bar"></div>

  <h2 class="heading right-title" style="top:347px">How we work. . .</h2>
  <div class="block right-text" style="top:381px">
    <p>One of our local resource advisors will work one-on-one with you to fully understand your situation in order to find and recommend the best path to you. Our plan for you can be as simple or as intricate as you would like or need.</p>
  </div>

  <h2 class="heading right-title" style="top:504px">We are available to work</h2>
  <div class="block right-text" style="top:536px">
    <ul class="avail">
      <li>Over the phone</li>
      <li>Face-to-face</li>
      <li>Via e-mail</li>
      <li>Or whatever makes you the most comfortable</li>
    </ul>
  </div>

  <h2 class="heading right-title" style="top:642px">What does this cost?</h2>
  <div class="block right-text" style="top:673px">
    <p>At Brookline Care Partners we offer our planning and resource referral services at no charge to you and your family.</p>
  </div>

  <h2 class="heading right-title" style="top:740px">How do I get started?</h2>
  <div class="block right-text" style="top:774px">
    <p>Simply call (800) 555-0142<br>or email us at<br>hello@brooklinecarepartners.com</p>
  </div>
</body>
</html>
```